Logo for Equipment and Auto parts seller
Crestline Supply and Machinery Corporation
Logo for Equipment and Auto parts seller - Automotive
Creative Brief
Simple
Julien Marceau
Operations Manager
Toliso
Julien.Marceau@cslmcorp.net

```html
<!DOCTYPE html>
<html lang="en">
<head>
<meta charset="utf-8">
<title>Crestline Supply and Machinery Corporation – Business Card</title>
<link rel="stylesheet" href="https://fonts.googleapis.com/css2?family=Montserrat:wght@400;600;800&display=swap">
<style>
  :root {
    --bg: #e7e5e2;
    --purple: #3d3f8f;
    --purple-dark: #2d2f72;
    --green: #7cc243;
    --white: #ffffff;
    --ink: #3a3a4a;
    --muted: #6b6b78;
    --black: #1d1e20;
  }
  * { margin: 0; padding: 0; box-sizing: border-box; }
  html, body { width: 1200px; height: 901px; overflow: hidden; }
  body {
    background: var(--bg);
    font-family: "Montserrat", Arial, sans-serif;
    position: relative;
  }
  .card {
    position: absolute;
    top: 135px;
    width: 360px;
    height: 630px;
    border-radius: 22px;
    overflow: hidden;
    box-shadow: 0 10px 28px rgba(0,0,0,0.18);
  }
  .card-front { left: 180px; background: var(--white); }
  .card-back { left: 660px; background: var(--black); }

  .front-swoosh { position: absolute; top: 0; left: 0; width: 360px; height: 220px; }

  .brand {
    position: absolute;
    left: 0; right: 0;
    display: flex;
    align-items: center;
    justify-content: center;
    gap: 10px;
  }
  .brand-front { top: 222px; }
  .brand-name {
    font-weight: 800;
    font-size: 44px;
    letter-spacing: 2px;
    color: var(--purple);
  }
  .brand-dot {
    width: 16px; height: 16px;
    border-radius: 50%;
    background: var(--green);
  }
  .company-name {
    position: absolute;
    top: 284px; left: 30px; right: 30px;
    text-align: center;
    font-size: 10px;
    font-weight: 600;
    letter-spacing: 0.6px;
    color: var(--purple);
    text-transform: uppercase;
  }
  .person {
    position: absolute;
    top: 340px; left: 40px;
  }
  .person-name {
    font-size: 18px;
    font-weight: 600;
    letter-spacing: 1px;
    color: var(--ink);
    text-transform: uppercase;
  }
  .person-title {
    margin-top: 4px;
    font-size: 11px;
    color: var(--green);
    font-weight: 600;
  }
  .contact-list {
    position: absolute;
    top: 430px; left: 40px;
    list-style: none;
  }
  .contact-item {
    display: flex;
    align-items: center;
    gap: 10px;
    font-size: 11px;
    color: var(--muted);
    margin-bottom: 12px;
  }
  .contact-icon {
    width: 18px; height: 18px;
    border-radius: 50%;
    background: var(--purple);
    display: flex; align-items: center; justify-content: center;
    flex-shrink: 0;
  }
  .brand-back { top: 0; bottom: 0; }
  .brand-back .brand-name { color: var(--white); font-size: 56px; }
  .brand-back .brand-dot { width: 20px; height: 20px; }
</style>
</head>
<body>
  <section class="card card-front" aria-label="Business card front">
    <svg class="front-swoosh" viewBox="0 0 360 220" aria-hidden="true">
      <path d="M0 0 H360 V60 C250 60 120 110 0 170 Z" fill="var(--purple)"/>
      <path d="M0 170 C120 110 250 60 360 60 V92 C250 95 130 140 0 205 Z" fill="var(--green)"/>
    </svg>

    <div class="brand brand-front">
      <span class="brand-dot"></span>
      <span class="brand-name">CSLM</span>
    </div>
    <p class="company-name">Crestline Supply and Machinery Corporation</p>

    <div class="person">
      <h1 class="person-name">Julien Marceau</h1>
      <p class="person-title">Operations Manager</p>
    </div>

    <ul class="contact-list">
      <li class="contact-item">
        <span class="contact-icon">
          <svg width="10" height="10" viewBox="0 0 10 10"><path d="M5 0.5a3 3 0 0 0-3 3c0 2.3 3 6 3 6s3-3.7 3-6a3 3 0 0 0-3-3z" fill="#fff"/><circle cx="5" cy="3.5" r="1.1" fill="var(--purple)"/></svg>
        </span>
        12 Harbor Road, Toliso 4410
      </li>
      <li class="contact-item">
        <span class="contact-icon">
          <svg width="10" height="10" viewBox="0 0 10 10"><path d="M2 1l2 2-1 1.3a6 6 0 0 0 2.7 2.7L7 6l2 2-1.2 1.3C4.5 9 1 5.5.7 2.2z" fill="#fff"/></svg>
        </span>
        T 555 0142
      </li>
      <li class="contact-item">
        <span class="contact-icon">
          <svg width="10" height="10" viewBox="0 0 10 10"><rect x="3" y="0.8" width="4" height="8.4" rx="0.8" fill="#fff"/></svg>
        </span>
        M 555 0187
      </li>
      <li class="contact-item">
        <span class="contact-icon">
          <svg width="10" height="10" viewBox="0 0 10 10"><rect x="1" y="2.5" width="8" height="5.5" fill="#fff"/><path d="M1 2.5l4 3 4-3" stroke="var(--purple)" stroke-width="0.8" fill="none"/></svg>
        </span>
        Julien.Marceau@cslmcorp.net
      </li>
      <li class="contact-item">
        <span class="contact-icon">
          <svg width="10" height="10" viewBox="0 0 10 10"><circle cx="5" cy="5" r="3.6" stroke="#fff" stroke-width="0.9" fill="none"/><path d="M1.4 5h7.2M5 1.4c-1.6 2-1.6 5.2 0 7.2M5 1.4c1.6 2 1.6 5.2 0 7.2" stroke="#fff" stroke-width="0.7" fill="none"/></svg>
        </span>
        www.cslmcorp.net
      </li>
    </ul>
  </section>

  <section class="card card-back" aria-label="Business card back">
    <div class="brand brand-back">
      <span class="brand-dot"></span>
      <span class="brand-name">CSLM</span>
    </div>
  </section>
</body>
</html>
```